Conference banner for Kestrel training organisation

We empower everyday heroes.
We provide training that empowers individuals to create positive change in themselves, their community, and the world.
We need a large banner design to promote the organisation at conferences and events. We are open to ideas and creativity.
It may involve creatively displaying our logo only, or it may involve our logo and a summary of our products (Kestrel training, Calm Minds Field Care).
Size: 820mm width x 1790mm height
300dpi
Target Market(s)
Educators and frontline health, community, and social workers.
Industry/Entity Type
Training
Colors
Designer to choose colors to be used in the design.

```html
<!DOCTYPE html>
<html lang="en">
<head>
<meta charset="utf-8">
<title>Kestrel Training – Conference Banner</title>
<link rel="stylesheet" href="https://fonts.googleapis.com/css2?family=Antonio:wght@300;400;600&display=swap">
<style>
  :root {
    --crimson: #bc1c4f;
    --royal-blue: #2a69fb;
    --deep-blue: #0d1ee0;
    --shadow: #5a0f2a;
    --paper: #ffffff;
  }
  html, body {
    margin: 0;
    padding: 0;
    width: 1200px;
    height: 2620px;
    overflow: hidden;
    background: var(--paper);
  }
  .banner {
    position: relative;
    width: 1200px;
    height: 2620px;
    overflow: hidden;
    background: var(--paper);
  }
  .banner__art {
    position: absolute;
    inset: 0;
    display: block;
  }
  .shape--crimson { fill: var(--crimson); }
  .shape--blue { fill: var(--royal-blue); }
  .shape--deep { fill: var(--deep-blue); }
  .shape--shadow { fill: var(--shadow); opacity: .55; }

  .headline {
    font-family: "Antonio", "Arial Narrow", sans-serif;
  }
  .headline__outline {
    font-weight: 300;
    fill: none;
    stroke-width: 5;
    stroke-linejoin: miter;
  }
  .headline__outline--blue { stroke: var(--royal-blue); }
  .headline__outline--crimson { stroke: var(--crimson); }
  .headline__solid {
    font-weight: 400;
    fill: var(--royal-blue);
  }

  .brand-mark {
    font-family: "Antonio", "Arial Narrow", sans-serif;
    font-weight: 600;
    letter-spacing: 2px;
  }
  .brand-mark--corner { fill: var(--paper); }
  .brand-mark--feature { fill: var(--royal-blue); }
  .brand-mark__dot { fill: var(--royal-blue); }
</style>
</head>
<body>
<main class="banner">
  <svg class="banner__art" width="1200" height="2620" viewBox="0 0 1200 2620" aria-labelledby="banner-title">
    <title id="banner-title">Kestrel training – Kestrel Hub</title>

    <!-- Background bands -->
    <svg class="bands" x="0" y="0" width="1200" height="2620" viewBox="0 0 687 1500" preserveAspectRatio="none">
      <polygon class="shape--crimson" points="305,0 687,0 687,1500 130,1500 560,1090 535,840 590,292"/>
      <polygon class="shape--blue" points="258,0 305,0 590,292 578,325"/>
      <polygon class="shape--blue" points="672,0 687,0 687,350 535,840 445,740 578,325 590,292"/>
      <polygon class="shape--shadow" points="687,350 687,390 548,835 535,840"/>
      <polygon class="shape--deep" points="535,840 560,800 545,838"/>
      <polygon class="shape--blue" points="687,780 687,850 500,1240 475,1150 520,960"/>
      <polygon class="shape--shadow" points="687,850 687,890 505,1235 500,1240"/>
      <polygon class="shape--deep" points="475,1150 500,1240 490,1150"/>
      <polygon class="shape--blue" points="340,1500 687,1260 687,1420 560,1500"/>
      <polygon class="shape--shadow" points="687,1420 687,1440 590,1500 560,1500"/>
      <polygon class="shape--blue" points="125,1420 265,1310 300,1340 200,1500 125,1500"/>
      <polygon class="shape--deep" points="265,1310 300,1340 215,1440"/>
    </svg>

    <!-- Corner brand name -->
    <text class="brand-mark brand-mark--corner" x="958" y="170" font-size="46" text-anchor="middle">KESTREL HUB</text>

    <!-- Headline -->
    <g class="headline">
      <g class="headline__outline headline__outline--blue" transform="translate(-8,-6)">
        <text x="130" y="500" font-size="490" textLength="335" lengthAdjust="spacingAndGlyphs">KES</text>
        <text x="130" y="935" font-size="490" textLength="335" lengthAdjust="spacingAndGlyphs">TREL</text>
      </g>
      <g class="headline__outline headline__outline--crimson">
        <text x="130" y="500" font-size="490" textLength="335" lengthAdjust="spacingAndGlyphs">KES</text>
        <text x="130" y="935" font-size="490" textLength="335" lengthAdjust="spacingAndGlyphs">TREL</text>
      </g>

      <text class="headline__solid" x="140" y="1170" font-size="250" textLength="320" lengthAdjust="spacingAndGlyphs">TRAI</text>
      <text class="headline__solid" x="140" y="1406" font-size="250" textLength="320" lengthAdjust="spacingAndGlyphs">NING</text>
    </g>

    <!-- Feature brand name -->
    <g class="brand-mark brand-mark--feature">
      <circle class="brand-mark__dot" cx="160" cy="1855" r="48"/>
      <text x="235" y="1900" font-size="120">KESTREL HUB</text>
    </g>
  </svg>
</main>
</body>
</html>
```